New iOS App design for Boston Startup

We are looking for a new app design for our Zorvak app. The current app's design feels outdated and we like to add lots of new functionality and a new navigation as well. A complete overhaul therefore!
We want you to design 5 screens that will have changed the most. The complete wireframes of these 5 pages are attached in the requirements document.
Once the winning design is selected we will award the winner with the designing all other screens (40-50 screens based on the same design). This will be a separate project worth $1000. The winning designer can get more follow up work if both sides are happy about the cooperation.
We will give feedback as soon as the first screen has been uploaded for review. Final decision will be made only after all 5 screens are finished.
We hope you give it your best!
Note: will only communicate through PixelGuild (no skype),
Updates
Project Deadline Extended
Reason: Want to give designers a chance to submit their designs as I understand from some, the deadline is too close.
I have raised the award and introduced a 2nd price as well to make it worth your time. I hope you give it your best shot.
Project Deadline Extended
Reason: A few of you have asked for an extension of the deadline as time is running out. I will extend by one day. Tell me if you need more.
Industry/Entity Type
Startup
Requirements
Must have
- At least 1 screen before we can give you feedback.
Nice to have
- multiple options of 1 screen to get to a desirable design

```html
<!DOCTYPE html>
<html lang="en">
<head>
<meta charset="utf-8">
<title>Practice - SC</title>
<link rel="stylesheet" href="https://fonts.googleapis.com/css2?family=Roboto:wght@300;400;500&display=swap">
<style>
  :root {
    --canvas: #f2f4f7;
    --blue: #2188d8;
    --blue-deep: #1a78c6;
    --blue-light: #3cb0e8;
    --row-line: rgba(255, 255, 255, 0.18);
    --white: #ffffff;
    --tab-bg: #f7f7f7;
    --tab-icon: #555a60;
    --tab-active: #1f7fd0;
    --highlight: rgba(200, 230, 250, 0.55);
    --highlight-text: #3f8fcc;
  }
  * { box-sizing: border-box; margin: 0; padding: 0; }
  html, body {
    width: 1200px; height: 826px; overflow: hidden;
    background: var(--canvas);
    font-family: "Roboto", "Helvetica Neue", Arial, sans-serif;
  }
  .app-screen {
    position: absolute; left: 400px; top: 33px;
    width: 400px; height: 760px;
    background: linear-gradient(115deg, var(--blue-light) 0%, var(--blue-light) 34%, var(--blue) 34.2%, var(--blue-deep) 100%);
    display: flex; flex-direction: column;
    overflow: hidden;
    box-shadow: 0 10px 40px rgba(0, 40, 80, 0.15);
  }
  .status-bar {
    height: 22px; padding: 0 8px;
    display: flex; align-items: center; justify-content: space-between;
    color: var(--white); font-size: 12px;
  }
  .status-bar .carrier { display: flex; align-items: center; gap: 5px; }
  .status-bar .signal { letter-spacing: 1px; font-size: 10px; }
  .status-bar .battery { display: flex; align-items: center; gap: 5px; }
  .battery-icon { width: 24px; height: 11px; border: 1px solid var(--white); border-radius: 2px; padding: 1px; }
  .battery-icon span { display: block; width: 100%; height: 100%; background: var(--white); }
  .nav-bar {
    height: 48px; position: relative;
    display: flex; align-items: center; justify-content: center;
    color: var(--white);
    border-bottom: 1px solid var(--row-line);
  }
  .nav-back {
    position: absolute; left: 10px; top: 50%; transform: translateY(-50%);
    display: flex; align-items: center; gap: 4px; font-size: 17px; font-weight: 300;
  }
  .nav-title { font-size: 18px; font-weight: 500; }
  .lesson-list { list-style: none; flex: 1; display: flex; flex-direction: column; }
  .lesson-row {
    flex: 1; display: flex; align-items: center;
    padding: 0 14px 0 22px;
    border-bottom: 1px solid var(--row-line);
    color: var(--white); font-size: 17px; font-weight: 300;
  }
  .lesson-title { flex: 1; }
  .status-mark {
    width: 26px; height: 26px; border-radius: 50%; margin-right: 14px;
    display: flex; align-items: center; justify-content: center;
  }
  .status-mark.done { background: var(--white); }
  .status-mark.open { border: 1px solid rgba(255, 255, 255, 0.7); }
  .chevron { width: 8px; height: 14px; }
  .lesson-row.current { background: var(--highlight); color: var(--highlight-text); }
  .tab-bar {
    height: 60px; background: var(--tab-bg);
    border-top: 1px solid #dcdfe3;
    display: flex; justify-content: space-around; align-items: center;
  }
  .tab {
    display: flex; flex-direction: column; align-items: center; gap: 3px;
    font-size: 11px; font-weight: 500; color: var(--tab-icon);
  }
  .tab svg { width: 28px; height: 26px; }
  .tab.active { color: var(--tab-active); }
</style>
</head>
<body>
<main class="app-screen">
  <header class="status-bar">
    <div class="carrier"><span class="signal">●●●</span><span>NOVA</span>
      <svg width="13" height="10" viewBox="0 0 13 10"><path d="M1 3.5a8 8 0 0 1 11 0M3 5.8a5 5 0 0 1 7 0M5 8a2 2 0 0 1 3 0" fill="none" stroke="#fff" stroke-width="1.3"/></svg>
    </div>
    <span class="clock">4:21 PM</span>
    <div class="battery"><span>100%</span><div class="battery-icon"><span></span></div></div>
  </header>
  <nav class="nav-bar">
    <div class="nav-back">
      <svg width="11" height="18" viewBox="0 0 11 18"><path d="M9 2 2 9l7 7" fill="none" stroke="#fff" stroke-width="2.2"/></svg>
      <span>Back</span>
    </div>
    <h1 class="nav-title">Practice - SC</h1>
  </nav>
  <ul class="lesson-list">
    <li class="lesson-row"><span class="lesson-title">Lesson 1 - Sentence Correction</span><span class="status-mark done"><svg width="14" height="12" viewBox="0 0 14 12"><path d="M2 6l3.5 3.5L12 2" fill="none" stroke="#2188d8" stroke-width="2"/></svg></span><svg class="chevron" viewBox="0 0 8 14"><path d="M1 1l6 6-6 6" fill="none" stroke="rgba(255,255,255,.6)" stroke-width="1.5"/></svg></li>
    <li class="lesson-row"><span class="lesson-title">Lesson 2 - Sentence Correction</span><span class="status-mark done"><svg width="14" height="12" viewBox="0 0 14 12"><path d="M2 6l3.5 3.5L12 2" fill="none" stroke="#2188d8" stroke-width="2"/></svg></span><svg class="chevron" viewBox="0 0 8 14"><path d="M1 1l6 6-6 6" fill="none" stroke="rgba(255,255,255,.6)" stroke-width="1.5"/></svg></li>
    <li class="lesson-row"><span class="lesson-title">Lesson 3 - Sentence Correction</span><span class="status-mark open"></span><svg class="chevron" viewBox="0 0 8 14"><path d="M1 1l6 6-6 6" fill="none" stroke="rgba(255,255,255,.6)" stroke-width="1.5"/></svg></li>
    <li class="lesson-row"><span class="lesson-title">Lesson 4 - Sentence Correction</span><span class="status-mark open"></span><svg class="chevron" viewBox="0 0 8 14"><path d="M1 1l6 6-6 6" fill="none" stroke="rgba(255,255,255,.6)" stroke-width="1.5"/></svg></li>
    <li class="lesson-row"><span class="lesson-title">Lesson 5 - Sentence Correction</span><span class="status-mark done"><svg width="14" height="12" viewBox="0 0 14 12"><path d="M2 6l3.5 3.5L12 2" fill="none" stroke="#2188d8" stroke-width="2"/></svg></span><svg class="chevron" viewBox="0 0 8 14"><path d="M1 1l6 6-6 6" fill="none" stroke="rgba(255,255,255,.6)" stroke-width="1.5"/></svg></li>
    <li class="lesson-row"><span class="lesson-title">Lesson 6 - Sentence Correction</span><span class="status-mark open"></span><svg class="chevron" viewBox="0 0 8 14"><path d="M1 1l6 6-6 6" fill="none" stroke="rgba(255,255,255,.6)" stroke-width="1.5"/></svg></li>
    <li class="lesson-row"><span class="lesson-title">Lesson 7 - Sentence Correction</span><span class="status-mark open"></span><svg class="chevron" viewBox="0 0 8 14"><path d="M1 1l6 6-6 6" fill="none" stroke="rgba(255,255,255,.6)" stroke-width="1.5"/></svg></li>
    <li class="lesson-row"><span class="lesson-title">Lesson 8 - Sentence Correction</span><span class="status-mark done"><svg width="14" height="12" viewBox="0 0 14 12"><path d="M2 6l3.5 3.5L12 2" fill="none" stroke="#2188d8" stroke-width="2"/></svg></span><svg class="chevron" viewBox="0 0 8 14"><path d="M1 1l6 6-6 6" fill="none" stroke="rgba(255,255,255,.6)" stroke-width="1.5"/></svg></li>
    <li class="lesson-row"><span class="lesson-title">Lesson 9 - Sentence Correction</span><span class="status-mark done"><svg width="14" height="12" viewBox="0 0 14 12"><path d="M2 6l3.5 3.5L12 2" fill="none" stroke="#2188d8" stroke-width="2"/></svg></span><svg class="chevron" viewBox="0 0 8 14"><path d="M1 1l6 6-6 6" fill="none" stroke="rgba(255,255,255,.6)" stroke-width="1.5"/></svg></li>
    <li class="lesson-row current"><span class="lesson-title">Lesson 10 - Sentence Correction</span><svg class="chevron" viewBox="0 0 8 14"><path d="M1 1l6 6-6 6" fill="none" stroke="rgba(255,255,255,.8)" stroke-width="1.5"/></svg></li>
  </ul>
  <footer class="tab-bar">
    <div class="tab"><svg viewBox="0 0 28 26"><path d="M3 13 14 3l11 10h-3v10h-6v-7h-4v7H6V13z" fill="#555a60"/></svg><span>Home</span></div>
    <div class="tab"><svg viewBox="0 0 28 26"><path d="M14 6C10 3 6 3 2 4v17c4-1 8-1 12 2 4-3 8-3 12-2V4c-4-1-8-1-12 2zm0 0v17" fill="none" stroke="#555a60" stroke-width="1.4"/></svg><span>Theory</span></div>
    <div class="tab active"><svg viewBox="0 0 28 26"><path d="M14 2 25 7 14 12 3 7z M3 12l11 5 11-5 M3 17l11 5 11-5" fill="none" stroke="#1f7fd0" stroke-width="2.4" stroke-linejoin="round"/></svg><span>Practice</span></div>
    <div class="tab"><svg viewBox="0 0 28 26"><path d="M8 7h12a6 6 0 0 1 6 7l-1 5a3 3 0 0 1-5 1l-3-3h-6l-3 3a3 3 0 0 1-5-1l-1-5a6 6 0 0 1 6-7z" fill="#555a60"/><path d="M7 12h4M9 10v4" stroke="#f7f7f7" stroke-width="1.5"/><circle cx="19" cy="11" r="1.2" fill="#f7f7f7"/><circle cx="21" cy="13.5" r="1.2" fill="#f7f7f7"/></svg><span>Games</span></div>
    <div class="tab"><svg viewBox="0 0 28 26"><path d="M8 20a6 6 0 0 1 0-12 7 7 0 0 1 13 1 5.5 5.5 0 0 1 0 11z" fill="#555a60"/><path d="M10 14l3 3 6-6" fill="none" stroke="#f7f7f7" stroke-width="2"/></svg><span>Test</span></div>
  </footer>
</main>
</body>
</html>
```